Commercial Post Cards

We are looking for 3 postcards that are similar but target 3 commercial property types. they will be 6x9 cards can be front and back or not.
1. Hotel Postcard – Quillmark / Bed Bug Protection
Use the attached Quillmark sample as the primary direction.
The focus should be:
Proactive bed bug prevention and control
Protecting guests and the hotel's reputation
Regular inspections
Documentation and risk management
Professional commercial pest management
The backside should transition into our General Pest Control services, showing that we can be the hotel's complete pest management provider beyond just bed bugs.
2. Apartment Complex Postcard
Target apartment owners, property managers, and management companies.
Focus on:
General pest control
Bed bug control
Rodent control
Preventative pest management
Protecting residents and the property
Reliable, ongoing service and documentation
The message should position us as a full-service pest management partner for multifamily properties.

3. Commercial Building Postcard
Target office buildings, banks, storage facilities, and other commercial properties.

Focus on:
General commercial pest control
Rodent control
Fly management
Recurring service programs
Protecting the property, employees, customers, and reputation

Overall Direction
All three postcards should have a consistent brand and visual style, but each should feel specifically designed for its target market.

We want the messaging to communicate:
Professional • Reliable • Proactive • Locally Owned & Operated • Serving Since 2017

The goal is not to overwhelm the reader with information. These should be marketing pieces that quickly communicate the problem we solve, our expertise, and why a commercial property should contact us.

I have included some of our marketing materials for help with what we do.

```html
<!DOCTYPE html>
<html lang="en">
<head>
<meta charset="utf-8">
<title>General Pest Solutions – Ridgeline Pest Control</title>
<link href="https://fonts.googleapis.com/css2?family=Bebas+Neue&family=Arimo:wght@700&display=swap" rel="stylesheet">
<style>
  :root{
    --orange:#fb5314;
    --ink:#1f1f1f;
    --charcoal:#2b2b2d;
    --white:#ffffff;
    --rule:#2a2a2a;
  }
  *{box-sizing:border-box;margin:0;padding:0}
  html,body{width:1200px;height:800px;overflow:hidden;background:var(--white)}
  .card{position:relative;width:1200px;height:800px;background:var(--white);overflow:hidden}

  .team-photo{
    position:absolute;left:740px;top:150px;width:460px;height:560px;
    background:
      linear-gradient(180deg,#f7fafc 0%,#d9e6f0 22%,#e8e2d2 45%,#dcd2bd 62%,#f08a45 72%,#cfc7b8 82%,#ece8e2 100%);
    -webkit-mask-image:linear-gradient(90deg,transparent 0%,#000 32%),linear-gradient(180deg,#000 75%,transparent 100%);
    -webkit-mask-composite:source-in;
    mask-image:linear-gradient(90deg,transparent 0%,#000 32%),linear-gradient(180deg,#000 75%,transparent 100%);
    mask-composite:intersect;
  }

  .headline{
    position:absolute;left:205px;top:52px;
    font-family:'Bebas Neue',sans-serif;font-size:60px;line-height:1;color:var(--ink);letter-spacing:.5px;
  }
  .headline .accent{color:var(--orange)}

  .brand{
    position:absolute;left:850px;top:128px;display:flex;align-items:center;gap:12px;
    font-family:'Bebas Neue',sans-serif;font-size:46px;line-height:1;color:var(--ink);
  }
  .brand-mark{width:26px;height:26px;background:var(--orange)}

  .service-row{position:absolute;left:55px;width:733px}
  .service-row.first{top:113px}
  .service-row.second{top:422px}
  .icon-band{height:80px;background:var(--orange);display:flex}
  .icon-cell{flex:1;display:flex;align-items:center;justify-content:center;position:relative}
  .icon-cell + .icon-cell::before{
    content:"";position:absolute;left:0;top:8px;bottom:8px;width:1.5px;background:var(--rule);
  }
  .shield{width:60px;height:70px}

  .text-band{display:flex;margin-top:10px}
  .service{flex:1;text-align:center;position:relative;padding:0 8px}
  .service + .service::before{
    content:"";position:absolute;left:0;top:0;bottom:0;width:1.5px;background:#bdbdbd;
  }
  .service-title{
    height:90px;display:flex;align-items:center;justify-content:center;
    font-family:'Bebas Neue',sans-serif;font-size:33px;line-height:28px;color:var(--orange);
  }
  .service-text{
    margin-top:6px;height:78px;
    font-family:'Arimo',Arial,sans-serif;font-size:15.5px;line-height:18.7px;color:var(--ink);
  }

  .values-bar{
    position:absolute;left:0;bottom:0;width:1200px;height:78px;background:var(--charcoal);
    display:flex;align-items:center;justify-content:center;
    font-family:'Bebas Neue',sans-serif;font-size:24px;letter-spacing:1.2px;color:var(--white);
  }
</style>
</head>
<body>
<svg width="0" height="0" style="position:absolute">
  <defs>
    <symbol id="shield-base" viewBox="0 0 60 70">
      <path d="M30 2 L56 12 V38 C56 54 44 63 30 68 C16 63 4 54 4 38 V12 Z" fill="#ffffff"/>
      <path d="M30 7 L52 15.5 V38 C52 51 42 59 30 63.5 C18 59 8 51 8 38 V15.5 Z" fill="#fb5314"/>
      <path d="M30 11 L48.5 18 V38 C48.5 49 40 56 30 60 C20 56 11.5 49 11.5 38 V18 Z" fill="#1f1f1f"/>
    </symbol>
  </defs>
</svg>

<div class="card">
  <div class="team-photo" role="img" aria-label="Photo of the pest control team in orange uniforms standing in front of a house with two service vans"></div>

  <h1 class="headline">General Pest <span class="accent">Solutions</span></h1>

  <div class="brand"><span class="brand-mark"></span>Ridgeline Pest Control</div>

  <section class="service-row first">
    <div class="icon-band">
      <div class="icon-cell"><svg class="shield" viewBox="0 0 60 70"><use href="#shield-base"/><circle cx="30" cy="28" r="3" fill="#fff"/><circle cx="30" cy="35" r="3.5" fill="#fff"/><circle cx="30" cy="44" r="5" fill="#fff"/></svg></div>
      <div class="icon-cell"><svg class="shield" viewBox="0 0 60 70"><use href="#shield-base"/><ellipse cx="30" cy="37" rx="11" ry="7" fill="#fff"/></svg></div>
      <div class="icon-cell"><svg class="shield" viewBox="0 0 60 70"><use href="#shield-base"/><ellipse cx="30" cy="39" rx="8" ry="10" fill="#fff"/><circle cx="30" cy="27" r="3.5" fill="#fff"/></svg></div>
      <div class="icon-cell"><svg class="shield" viewBox="0 0 60 70"><use href="#shield-base"/><ellipse cx="25" cy="38" rx="5" ry="9" fill="#fff"/><ellipse cx="35" cy="38" rx="5" ry="9" fill="#fff"/><circle cx="30" cy="27" r="3.5" fill="#fff"/></svg></div>
    </div>
    <div class="text-band">
      <div class="service"><h2 class="service-title">General<br>Insect<br>Control</h2><p class="service-text">Ants, spiders, cockroaches, and other common pests.</p></div>
      <div class="service"><h2 class="service-title">Mouse &amp;<br>Rodent<br>Control</h2><p class="service-text">Inspection, control, and ongoing monitoring.</p></div>
      <div class="service"><h2 class="service-title">Bed Bug<br>Control</h2><p class="service-text">Inspection, treatment, prevention, and ongoing monitoring.</p></div>
      <div class="service"><h2 class="service-title">Fly Control &amp;<br>Management</h2><p class="service-text">Prevention and ongoing fly maintenance.</p></div>
    </div>
  </section>

  <section class="service-row second">
    <div class="icon-band">
      <div class="icon-cell"><svg class="shield" viewBox="0 0 60 70"><use href="#shield-base"/><rect x="21" y="25" width="18" height="24" rx="2" fill="#fff"/><rect x="26" y="22" width="8" height="5" rx="1" fill="#fff" stroke="#1f1f1f" stroke-width="1"/><path d="M24 33h12M24 38h12M24 43h8" stroke="#1f1f1f" stroke-width="1.6"/></svg></div>
      <div class="icon-cell"><svg class="shield" viewBox="0 0 60 70"><use href="#shield-base"/><rect x="22" y="22" width="16" height="28" fill="#fff"/><rect x="17" y="32" width="6" height="18" fill="#fff"/><path d="M25 26h3M32 26h3M25 31h3M32 31h3M25 36h3M32 36h3M25 41h3M32 41h3" stroke="#1f1f1f" stroke-width="2"/><rect x="28" y="45" width="4" height="5" fill="#1f1f1f"/></svg></div>
      <div class="icon-cell"><svg class="shield" viewBox="0 0 60 70"><use href="#shield-base"/><circle cx="32" cy="32" r="9" fill="none" stroke="#fff" stroke-width="3"/><path d="M25.5 38.5 L19 45" stroke="#fff" stroke-width="4" stroke-linecap="round"/><path d="M32 27 L38 38 H26 Z" fill="#fff"/><path d="M32 30.5v4" stroke="#1f1f1f" stroke-width="1.5"/><circle cx="32" cy="36.2" r=".9" fill="#1f1f1f"/></svg></div>
      <div class="icon-cell"><svg class="shield" viewBox="0 0 60 70"><use href="#shield-base"/><rect x="19" y="24" width="22" height="21" rx="2" fill="#fff"/><rect x="19" y="24" width="22" height="5" fill="#fff"/><path d="M19 29.5h22" stroke="#1f1f1f" stroke-width="1.2"/><path d="M22 33h3M27 33h3M32 33h3M22 37h3M27 37h3M22 41h3" stroke="#1f1f1f" stroke-width="2"/><circle cx="38" cy="43" r="6" fill="#fff" stroke="#1f1f1f" stroke-width="1.5"/><path d="M38 40v3h2.5" stroke="#1f1f1f" stroke-width="1.4" fill="none"/></svg></div>
    </div>
    <div class="text-band">
      <div class="service"><h2 class="service-title">Preventative<br>Pest<br>Management</h2><p class="service-text">Routine inspections and proactive treatments.</p></div>
      <div class="service"><h2 class="service-title">Exterior<br>Pest<br>Control</h2><p class="service-text">Perimeter treatments to help prevent pests from entering.</p></div>
      <div class="service"><h2 class="service-title">Commercial<br>Pest<br>Inspections</h2><p class="service-text">Identify pest activity and potential risk areas.</p></div>
      <div class="service"><h2 class="service-title">Ongoing<br>Service<br>Programs</h2><p class="service-text">Scheduled service tailored to your property's needs.</p></div>
    </div>
  </section>

  <footer class="values-bar">Professional • Reliable • Proactive • Locally Owned &amp; Operated • Serving Since 2017</footer>
</div>
</body>
</html>
```